Webdesign für Steuerberaterin
Zielgruppe
Ich bin Steuerberaterin. Meine Zielgruppe sind sowohl Privatpersonen als auch Unternehmer sowie Männer und Frauen.
Aufgabenstellung
Bitte mein Logo und Foto mit berücksichtigen. Ich möchte keine Website, auf der alle 'Reiter' als eine Seite von oben nach unten durchlaufen. Sondern wirklich einzelne, voneinander getrennte Seiten.

```html
<!DOCTYPE html>
<html lang="de">
<head>
<meta charset="utf-8">
<title>Steuerberaterin – Startseite</title>
<link rel="stylesheet" href="https://fonts.googleapis.com/css2?family=PT+Sans:wght@400;700&family=Tinos&display=swap">
<style>
  :root {
    --sidebar: #1c1a1f;
    --gold: #b08a2e;
    --gold-rule: #c9a52a;
    --gold-band: #dfb83a;
    --text: #555457;
    --white: #ffffff;
    --cloud: #3a383d;
  }
  * { margin: 0; padding: 0; box-sizing: border-box; }
  html, body { width: 1200px; height: 768px; overflow: hidden; background: var(--white); }
  body { position: relative; font-family: "PT Sans", Tahoma, sans-serif; color: var(--text); }

  .sidebar { position: absolute; left: 0; top: 0; width: 307px; height: 743px; background: var(--sidebar); }
  .footer-band { position: absolute; left: 0; bottom: 0; width: 1200px; height: 25px; background: var(--gold-band); }

  .brand { position: absolute; left: 277px; top: 29px; width: 129px; height: 142px; background: var(--white);
    display: flex; flex-direction: column; align-items: center; justify-content: center; gap: 10px; }
  .brand-dot { width: 26px; height: 26px; border-radius: 50%; background: var(--gold); }
  .brand-name { font-size: 14px; color: var(--gold); text-align: center; line-height: 1.2; }

  .main-nav a { position: absolute; left: 92px; font-size: 14px; color: var(--gold); text-decoration: none; }
  .legal { position: absolute; left: 92px; top: 466px; font-size: 14px; color: var(--gold); }
  .legal a { color: var(--gold); text-decoration: none; }
  .legal span { margin: 0 8px; }

  .portrait { position: absolute; left: 89px; top: 219px; width: 316px; height: 230px;
    background: linear-gradient(90deg, #d6d4d2, #f4f3f2 45%, #e2e0de 70%, #cfcdcb); }

  .word-cloud { position: absolute; left: 15px; top: 570px; width: 292px; height: 160px;
    background: radial-gradient(ellipse at 50% 45%, #3d3b40 0%, #2a282d 45%, var(--sidebar) 75%); }

  .welcome { position: absolute; left: 580px; width: 430px; }
  .welcome h1 { position: absolute; left: 0; top: 102px; width: 430px; text-align: center;
    font-family: "Tinos", "Times New Roman", serif; font-weight: 400; font-size: 23px; color: var(--gold); }
  .welcome .rule { position: absolute; left: 0; top: 155px; width: 430px; height: 2px; background: var(--gold-rule); }
  .welcome .lead { position: absolute; left: 0; top: 207px; font-size: 15.5px; font-weight: 700; white-space: nowrap; }
  .welcome p { position: absolute; left: 0; font-size: 15px; line-height: 20.5px; white-space: nowrap; }
</style>
</head>
<body>
  <aside class="sidebar">
    <nav class="main-nav">
      <a href="#" style="top:72px">Über mich</a>
      <a href="#" style="top:114px">Leistungen</a>
      <a href="#" style="top:156px">Kontakt</a>
    </nav>
    <div class="legal"><a href="#">Impressum</a><span>|</span><a href="#">Datenschutz</a></div>
    <div class="word-cloud" role="img" aria-label="Dekorative Wortwolke mit Steuerbegriffen"></div>
  </aside>

  <div class="brand">
    <div class="brand-dot"></div>
    <div class="brand-name">Sabine Hortmann</div>
  </div>

  <div class="portrait" role="img" aria-label="Porträtfoto der Steuerberaterin vor heller Steinwand"></div>

  <main class="welcome">
    <h1>Schön, dass Sie da sind</h1>
    <div class="rule"></div>
    <div class="lead">Ich freue mich, dass Sie den Weg zu mir gefunden haben!</div>
    <p style="top:250px">Sie sind bei mir genau richtig:<br>Egal, ob Sie Privatperson sind, die Ihre Einkommensteuer-Erklärung<br>in vertrauensvolle Hände geben möchte,<br>oder Unternehmer, der sich z.B. das „Rundum-Sorglos-Paket“<br>mit Buchführung, Jahresabschluss und Steuererklärungen wünscht.</p>
    <p style="top:377px">Schauen Sie sich hier gerne um und melden Sie sich bei mir<br>– ich bin bei jedem steuerlichen Thema gerne Ihr kompetenter<br>und zuverlässiger Ansprechpartner.</p>
    <p style="top:464px">Für mich ist es eine Selbstverständlichkeit,<br>dass ich auch nach mehr als 12 Jahren Berufserfahrung<br>durch permanente Fortbildungen immer auf dem aktuellsten Stand<br>der relevanten Gesetze und Verordnungen bin.<br>Nur so kann ich Sie bestmöglich beraten.</p>
  </main>

  <div class="footer-band"></div>
</body>
</html>
```